Online Art Gallery & Art Management Firm looking for a business card

I'm launching an online art gallery (paintings, photography, drawings, furniture, books, ...) where people can buy all types of art. It's a platform where young and unknown artists can showcase their oeuvre.

Additionally, the venture will act as my advising company for artists. I help them out with their business side of life and become their representative.

The company name: The Velmora House
Logo is attached

I'm looking for something very classy and upmarket.
Updates

Reason: Logo wasn't finished yet...

The design should include the following information: - Name: Pieter Drovensky - Title: Founder - Mobile: +32 (0) 485 613 204 - E-mail: pieter@velmora-house.net - Website www.velmora-house.net I prefer the have the logo (without website) on the one side and the information on the other. Best regards Pieter

Target Market(s)

Art buyers / art dealers / artists / middle class / upmarket /

Industry/Entity Type

Artists

Colors

Designer to choose colors to be used in the design.

Requirements
Must have
• Must communicate credibility, trust and integrity
Nice to have
• Something classy, chique
Should not have
• Nothing to artistic or creative

```html
<!DOCTYPE html>
<html lang="en">
<head>
<meta charset="utf-8">
<title>The Velmora House — Business Card</title>
<link rel="stylesheet" href="https://fonts.googleapis.com/css2?family=Lato:ital,wght@0,300;0,400;0,700;0,900;1,700&display=swap">
<style>
  :root {
    --backdrop: #3a3a3c;
    --card: #f7f7f7;
    --card-edge: #ececec;
    --band-light: #e4e4e4;
    --band-dark: #c9c9c9;
    --ink: #111111;
    --ink-soft: #4a4a4a;
    --rule: #3c3c3c;
  }
  * { margin: 0; padding: 0; box-sizing: border-box; }
  html, body {
    width: 1200px;
    height: 926px;
    overflow: hidden;
    background: var(--backdrop);
    font-family: "Lato", Arial, sans-serif;
  }
  .canvas {
    width: 1200px;
    height: 926px;
    display: flex;
    flex-direction: column;
    align-items: center;
    justify-content: center;
    gap: 46px;
  }
  .card {
    position: relative;
    width: 700px;
    height: 400px;
    background: linear-gradient(180deg, var(--card) 0%, var(--card-edge) 100%);
    overflow: hidden;
  }
  .wordmark {
    font-family: "Lato", Arial, sans-serif;
    font-weight: 300;
    color: var(--ink);
    text-transform: uppercase;
    letter-spacing: 0.28em;
    white-space: nowrap;
  }
  .card--front {
    display: flex;
    align-items: center;
    justify-content: center;
  }
  .card--front .wordmark { font-size: 30px; }

  .band {
    position: absolute;
    left: 0;
    right: 0;
    top: 104px;
    height: 138px;
    background: linear-gradient(90deg, var(--band-light) 0%, var(--band-light) 35%, var(--band-dark) 100%);
    display: flex;
    align-items: center;
  }
  .contact {
    width: 300px;
    padding-right: 24px;
    text-align: right;
    color: var(--ink-soft);
  }
  .contact__name {
    font-weight: 900;
    font-size: 18px;
    letter-spacing: 0.04em;
    color: var(--ink);
    text-transform: uppercase;
    line-height: 1.1;
  }
  .contact__title {
    font-size: 12px;
    letter-spacing: 0.08em;
    text-transform: uppercase;
    margin-bottom: 4px;
  }
  .contact__line {
    font-size: 12.5px;
    font-weight: 400;
    line-height: 1.35;
    white-space: nowrap;
  }
  .contact__label {
    font-weight: 700;
    font-style: italic;
    color: var(--ink);
    margin-right: 4px;
  }
  .divider {
    width: 1px;
    height: 96px;
    background: var(--rule);
  }
  .band .wordmark {
    font-size: 21px;
    padding-left: 28px;
    letter-spacing: 0.22em;
  }
</style>
</head>
<body>
  <main class="canvas">
    <section class="card card--front" aria-label="Card front">
      <span class="wordmark">The Velmora House</span>
    </section>

    <section class="card card--back" aria-label="Card back">
      <div class="band">
        <div class="contact">
          <p class="contact__name">Pieter Drovensky</p>
          <p class="contact__title">Founder</p>
          <p class="contact__line"><span class="contact__label">mobile:</span>+32 (0) 485 613 204</p>
          <p class="contact__line"><span class="contact__label">e-mail:</span>pieter@velmora-house.net</p>
          <p class="contact__line"><span class="contact__label">website:</span>www.velmora-house.net</p>
        </div>
        <div class="divider"></div>
        <span class="wordmark">The Velmora House</span>
      </div>
    </section>
  </main>
</body>
</html>
```